Real Estate Listing Signs for standard Yard arms

I need real estate listing signs done, for the standard sized sign to be hung beneath a white yard arm. To match existing logo. Information to be included:
-Logo
-Business name
-Phone number
-Marden Fosk Tundra Circle & Marden Fosk realty logos (smaller print)

Colors to be Red and anywhere in the gray scale between black and white, or a combination of those.

Target Market(s)

Drive by visuals

Industry/Entity Type

Real Estate Agent

Colors

Designer to choose only greyscale colors for use in the design.

Requirements
Must have
• My Logo and business name in same/similar font to whats provided, the MF tundra circle logo (small on bottom or corner somewhere), My phone number, and a decent amount of red coloration on the sign.

```html
<!DOCTYPE html>
<html lang="en">
<head>
<meta charset="utf-8">
<title>Vesterly Realty – Yard Sign</title>
<link rel="stylesheet" href="https://fonts.googleapis.com/css2?family=Antonio:wght@400;500&family=Cinzel:wght@700;900&display=swap">
<style>
  :root {
    --red: #ec2a33;
    --black: #000000;
    --light-gray: #e2e3e5;
    --name-gray: #e6e6e6;
    --white: #ffffff;
  }
  html, body { margin: 0; padding: 0; overflow: hidden; background: var(--white); }
  .sign {
    position: relative;
    width: 1200px;
    height: 894px;
    overflow: hidden;
    background: var(--red);
  }
  .sign__shapes { position: absolute; inset: 0; }
  .agent-name {
    position: absolute; left: 0; right: 0; top: 22px;
    margin: 0; text-align: center;
    font-family: "Cinzel", serif; font-weight: 700;
    font-size: 64px; line-height: 1; letter-spacing: 1px;
    color: var(--name-gray);
  }
  .phone, .email {
    position: absolute; top: 136px; margin: 0;
    font-family: "Antonio", sans-serif; font-weight: 500;
    line-height: 1; color: var(--black);
  }
  .phone { left: 66px; font-size: 96px; top: 140px; }
  .email { left: 668px; font-size: 84px; top: 136px; }
  .brand {
    position: absolute; left: 262px; top: 380px;
    display: flex; align-items: center; gap: 46px;
  }
  .brand__mark { width: 186px; height: 186px; background: var(--red); }
  .brand__name {
    margin: 0;
    font-family: "Cinzel", serif; font-weight: 900;
    font-size: 84px; line-height: 0.98; color: var(--black);
  }
  .office {
    position: absolute; left: 68px; top: 770px; margin: 0;
    font-family: "Antonio", sans-serif; font-weight: 500;
    color: var(--white); line-height: 1;
  }
  .office__group { display: block; font-size: 52px; }
  .office__realty { display: block; font-size: 20px; margin-top: 6px; letter-spacing: 0.5px; }
  .disclaimer {
    position: absolute; right: 88px; top: 782px; margin: 0;
    text-align: right;
    font-family: "Antonio", sans-serif; font-weight: 400;
    font-size: 38px; line-height: 1.0; color: var(--white);
  }
</style>
</head>
<body>
<main class="sign">
  <svg class="sign__shapes" width="1200" height="894" viewBox="0 0 1200 894" aria-hidden="true">
    <rect class="band-top" x="0" y="0" width="1200" height="113" fill="var(--black)"/>
    <rect class="band-contact" x="0" y="113" width="1200" height="140" fill="var(--light-gray)"/>
    <rect class="band-bottom" x="0" y="742" width="1200" height="152" fill="var(--black)"/>
    <rect class="panel" x="128" y="267" width="944" height="461" fill="var(--white)"/>
    <polygon class="ribbon-top" points="536,113 665,233 665,253 536,253" fill="var(--red)"/>
    <polygon class="ribbon-upper" points="536,267 665,267 665,352 600,288 536,352" fill="var(--red)"/>
    <polygon class="ribbon-lower" points="536,728 536,658 600,724 665,658 665,728" fill="var(--red)"/>
    <rect class="ribbon-foot" x="536" y="742" width="129" height="152" fill="var(--red)"/>
  </svg>

  <h1 class="agent-name">Jordan Vesterly</h1>
  <p class="phone">907-555-0148</p>
  <p class="email">jv@vesterly.com</p>

  <div class="brand">
    <div class="brand__mark"></div>
    <p class="brand__name">Vesterly<br>Realty</p>
  </div>

  <p class="office">
    <span class="office__group">MF TUNDRA CIRCLE</span>
    <span class="office__realty">MARDEN FOSK REALTY</span>
  </p>

  <p class="disclaimer">Each Office Independently<br>Owned and Operated</p>
</main>
</body>
</html>
```